Commercial wall and ceiling contractor needs website

Construction trade companies are notoriously behind the rest of the world when it comes to using current technology to run their businesses; we are not one of those companies. We are a walls and ceilings contractor using up to date communications technologies and applying them unlike any other in our trade. As simple as it sounds, and it really is that simple, it is still a new idea in the trade. We are moving our customers towards communicating with us through a single point of contact using text and email; we distribute information to the appropriate internal party on our end. We need a website that generally appears traditionally familiar to the visitor while also expresses a fresh new approach and edginess to the trade business.

Target Market(s)

General contractors looking to get a bit of background info before inviting us to bid on their projects. This is not a high traffic environment. Their subsequent site visits will be primarily for contact info.

Industry/Entity Type

Construction Company

Number of Pages Required

3 page

Font styles to use
Sans Serif

Requirements
Must have
• The file I uploaded named "kolsite.docx" does not have to appear on the site in the same manner in which appears in the document file; but the info contained within that document does need to be represented on the site.

```html
<!DOCTYPE html>
<html lang="en">
<head>
<meta charset="utf-8">
<title>Brackwell Walls and Ceilings</title>
<link rel="stylesheet" href="https://fonts.googleapis.com/css2?family=Exo+2:wght@400;600;700&family=Montserrat:ital,wght@0,400;0,500;0,600;0,700;1,400&display=swap">
<style>
:root{
  --orange:#c8902b;
  --orange-dark:#a9741a;
  --green:#0c7a53;
  --ink:#2f2f2f;
  --muted:#6d6d6d;
  --light:#f2f2f2;
  --footer:#2c2c2c;
  --footer-field:#555;
  --blue-dark:#1f4f9c;
  --blue-light:#4fc3e6;
  --chart-green:#16a36a;
  --chart-lime:#7cc242;
}
*{box-sizing:border-box;margin:0;padding:0}
html,body{width:1200px;height:3719px;overflow:hidden}
body{position:relative;background:#fff;font-family:"Montserrat",sans-serif;color:var(--ink)}
.abs{position:absolute}
.heading{font-family:"Exo 2",sans-serif}

/* header */
.site-header{left:0;top:0;width:1200px;height:119px;background:#fff}
.brand{left:87px;top:30px;display:flex;align-items:center;gap:12px}
.brand-mark{width:26px;height:26px;background:var(--green)}
.brand-name{font-family:"Exo 2",sans-serif;font-weight:700;font-size:30px;color:var(--orange);letter-spacing:1px}
.header-call{left:735px;top:28px;font-size:17px;font-weight:600;color:var(--orange)}
.header-call b{color:var(--green);margin-left:8px}
.social{display:flex;gap:10px}
.social span{width:28px;height:28px;border:2px solid var(--orange);display:block}
.header-social{left:992px;top:24px}
.main-nav{left:484px;top:74px;display:flex;gap:42px;font-size:12px;font-weight:600;color:var(--ink);letter-spacing:.5px}
.main-nav .active{color:var(--orange)}

/* hero */
.hero{left:0;top:119px;width:1200px;height:558px;background:linear-gradient(90deg,#8d8d8d 0%,#b4b4b4 35%,#8a5a48 70%,#6f4536 100%)}
.hero-title{left:0;top:195px;width:1200px;text-align:center;font-family:"Exo 2",sans-serif;font-size:40px;line-height:52px;color:#fff;font-weight:400}
.hero-title b{font-weight:700}
.btn{display:inline-block;font-size:12px;font-weight:600;letter-spacing:.8px;text-align:center;line-height:32px;height:34px}
.btn-solid{background:var(--orange);color:#fff}
.btn-outline{border:2px solid var(--orange);color:var(--orange);line-height:30px}
.btn-white{background:#fff;color:var(--ink)}
.hero-btn{left:535px;top:321px;width:130px}
.hero-arrow{top:262px;width:20px;height:34px}
.hero-dots{left:570px;top:511px;display:flex;gap:5px}
.dot{width:13px;height:13px;border-radius:50%;border:2px solid #ccc}
.dot.on{background:#ccc}

/* about */
.about-photo{left:208px;top:774px;width:352px;height:372px;background:linear-gradient(160deg,#d9d9d9,#8e8e8e 60%,#7a5a3f)}
.section-title{font-family:"Exo 2",sans-serif;font-size:34px;font-weight:400;color:var(--orange)}
.section-title b{color:var(--green);font-weight:700}
.title-bracket{position:absolute;left:-18px;top:-22px;width:60px;height:62px}
.about-title{left:662px;top:814px}
.about-text{left:640px;top:900px;width:348px;font-size:12px;line-height:20px;color:var(--muted)}
.about-btn{left:640px;top:1086px;width:144px}

/* services */
.services{left:0;top:1215px;width:1200px;height:362px}
.service-title{font-family:"Exo 2",sans-serif;font-size:26px;font-weight:600;color:#fff;text-align:center}
.service-text{font-size:12px;line-height:19px;color:#fff;text-align:center}

/* why */
.why{left:0;top:1578px;width:1200px;height:1052px;background:var(--light)}
.why-title{left:508px;top:1612px}
.why-lead{left:0;top:1692px;width:1200px;text-align:center;font-size:15px;line-height:22px;color:var(--ink)}
.chart-label{font-size:12px;font-weight:600;line-height:16px;color:var(--ink)}
.why-text{font-size:12px;line-height:20px;color:var(--muted)}
.why-call{left:0;top:2464px;width:1200px;text-align:center;font-size:17px;font-weight:600;color:var(--orange)}
.why-call b{color:var(--green)}
.why-mail{left:0;top:2490px;width:1200px;text-align:center;font-size:12px;color:var(--muted)}

/* testimonial */
.testi-title{left:472px;top:2728px}
.quote-mark{left:0;top:2800px;width:1200px;text-align:center;font-family:"Exo 2",sans-serif;font-size:64px;line-height:60px;font-weight:700;color:var(--orange)}
.testi-text{left:240px;top:2872px;width:720px;text-align:center;font-style:italic;font-size:15px;line-height:23px;color:var(--ink)}
.testi-name{left:0;top:2974px;width:1200px;text-align:center;font-size:11px;font-weight:700;color:var(--orange);letter-spacing:1px}
.testi-dots{left:561px;top:3022px;display:flex;gap:6px}
.testi-dots .dot{border-color:#777}
.testi-dots .dot.on{background:#777}

/* footer */
.site-footer{left:0;top:3120px;width:1200px;height:599px;background:var(--footer)}
.footer-brand{left:500px;top:3200px}
.footer-head{font-size:15px;font-weight:600;color:#fff}
.footer-call{left:87px;top:3395px;font-size:24px;color:#fff}
.footer-small{font-size:12px;line-height:19px;color:#bdbdbd}
.quick-links{left:419px;top:3396px;list-style:none;font-size:12px;line-height:27px;color:#bdbdbd}
.quick-links .active{color:var(--orange)}
.field{background:var(--footer-field);height:30px;font-size:12px;color:#ddd;padding:7px 12px}
.send-btn{left:1057px;top:3537px;width:28px;height:28px;border-radius:50%;background:var(--orange)}
.footer-bottom{top:3638px;font-size:11px;color:#bdbdbd}
</style>
</head>
<body>

<header class="abs site-header">
  <div class="abs brand"><span class="brand-mark"></span><span class="brand-name">BRACKWELL</span></div>
  <div class="abs header-call">Call Us: <b>&#9742; 604-555-0182</b></div>
  <div class="abs social header-social"><span></span><span></span><span></span></div>
  <nav class="abs main-nav">
    <span class="active">HOME</span><span>ABOUT US</span><span>SERVICES</span><span>WHY BRACKWELL?</span><span>PROJECTS</span><span>CONTACT US</span>
  </nav>
</header>

<section class="abs hero" role="img" aria-label="Photo of a finished commercial interior with brick wall, large windows and suspended ceiling panel"></section>
<h1 class="abs hero-title">We are Commercial <b>Wall</b> and<br><b>Ceiling</b> Contractor</h1>
<a class="abs btn btn-solid hero-btn">CONTACT US</a>
<svg class="abs hero-arrow" style="left:86px" viewBox="0 0 20 34"><path d="M16 3 3 17l13 14" fill="none" stroke="#fff" stroke-width="3"/></svg>
<svg class="abs hero-arrow" style="left:1094px" viewBox="0 0 20 34"><path d="M4 3l13 14L4 31" fill="none" stroke="#fff" stroke-width="3"/></svg>
<div class="abs hero-dots"><span class="dot on"></span><span class="dot"></span><span class="dot"></span><span class="dot"></span></div>

<section>
  <div class="abs about-photo" role="img" aria-label="Photo of an open-plan office with workstations and a grid ceiling"></div>
  <h2 class="abs section-title about-title">
    <svg class="title-bracket" viewBox="0 0 60 62"><path d="M40 2H14L2 14v46h36" fill="none" stroke="var(--orange)" stroke-width="3"/></svg>
    About <b>Us</b></h2>
  <p class="abs about-text">Lorem Ipsum is simply dummy text of the printing and typesetting industry. Lorem Ipsum has been the industry's standard dummy text ever since the 1500s, when an unknown printer took a galley of type and scrambled it to make a type specimen book. It has survived not only five centuries, but also the leap into electronic typesetting, remaining essentially unchanged ...</p>
  <a class="abs btn btn-outline about-btn">DISCOVER MORE</a>
</section>

<section class="abs services">
  <svg width="1200" height="362" viewBox="0 0 1200 362" role="img" aria-label="Photos of wall framing and a finished ceiling, tinted in brand colours">
    <defs>
      <linearGradient id="wallTone" x1="0" x2="1"><stop offset="0" stop-color="#b9831f"/><stop offset="1" stop-color="#d6a03a"/></linearGradient>
      <linearGradient id="ceilTone" x1="0" x2="1"><stop offset="0" stop-color="#0b6f4b"/><stop offset="1" stop-color="#14946a"/></linearGradient>
    </defs>
    <polygon points="0,0 600,30 600,318 0,360" fill="url(#wallTone)"/>
    <polygon points="600,30 1200,0 1200,362 600,318" fill="url(#ceilTone)"/>
  </svg>
  <h3 class="abs service-title" style="left:150px;top:90px;width:300px">Walls</h3>
  <p class="abs service-text" style="left:110px;top:140px;width:380px">Lorem Ipsum is simply dummy text of the printing and typesetting industry. Lorem Ipsum has been the lorem industry's standard dummy when an ...</p>
  <a class="abs btn btn-white" style="left:248px;top:230px;width:108px">READ MORE</a>
  <h3 class="abs service-title" style="left:750px;top:90px;width:300px">Ceilings</h3>
  <p class="abs service-text" style="left:710px;top:140px;width:380px">Lorem Ipsum is simply dummy text of the printing and typesetting industry. Lorem Ipsum has been the lorem industry's standard dummy when an ...</p>
  <a class="abs btn btn-white" style="left:846px;top:230px;width:108px">READ MORE</a>
</section>

<section class="abs why"></section>
<h2 class="abs section-title why-title">
  <svg class="title-bracket" viewBox="0 0 60 62"><path d="M40 2H14L2 14v46h36" fill="none" stroke="var(--orange)" stroke-width="3"/></svg>
  Why <b>Brackwell?</b></h2>
<p class="abs why-lead">Today's communication landscape is dramatically different than it was a mere ten years ago.<br>We use our phones less and less for making calls.</p>

<svg class="abs" style="left:222px;top:1834px" width="200" height="200" viewBox="0 0 200 200">
  <circle cx="100" cy="100" r="84" fill="none" stroke="var(--blue-light)" stroke-width="16" stroke-dasharray="200 328" transform="rotate(180 100 100)"/>
  <circle cx="100" cy="100" r="84" fill="none" stroke="var(--blue-dark)" stroke-width="16" stroke-dasharray="170 358" transform="rotate(-60 100 100)"/>
  <circle cx="100" cy="100" r="84" fill="none" stroke="var(--chart-green)" stroke-width="16" stroke-dasharray="140 388" transform="rotate(60 100 100)"/>
  <circle cx="100" cy="100" r="72" fill="#e4e4e4"/>
  <path d="M100 100V28M100 100l62 36M100 100l-62 36" stroke="#fff" stroke-width="3"/>
  <circle cx="100" cy="100" r="24" fill="#fff" stroke="#ccc" stroke-width="2"/>
  <rect x="93" y="88" width="14" height="24" rx="2" fill="none" stroke="var(--chart-green)" stroke-width="2"/>
  <text x="70" y="70" font-family="Montserrat,sans-serif" font-size="22" fill="#555" text-anchor="middle">10x</text>
  <text x="70" y="82" font-family="Montserrat,sans-serif" font-size="7" fill="#777" text-anchor="middle">quicker</text>
  <text x="145" y="102" font-family="Montserrat,sans-serif" font-size="18" fill="#555" text-anchor="middle">90</text>
  <text x="145" y="113" font-family="Montserrat,sans-serif" font-size="6" fill="#777" text-anchor="middle">seconds avg</text>
  <text x="80" y="150" font-family="Montserrat,sans-serif" font-size="22" fill="#555" text-anchor="middle">5</text>
  <text x="105" y="148" font-family="Montserrat,sans-serif" font-size="7" fill="#777" text-anchor="middle">seconds</text>
</svg>
<div class="abs chart-label" style="left:87px;top:1786px;width:180px">Texting is 10x quicker than a phone call</div>
<div class="abs chart-label" style="left:482px;top:1882px;width:160px">Average Response Time for a Text is 90 Seconds (WDC)</div>
<div class="abs chart-label" style="left:87px;top:1970px;width:150px">On average, text Messages are read in under 5 seconds</div>
<p class="abs why-text" style="left:759px;top:1818px;width:370px">The average length of a phone call has sharply decreased since 2006. That's because it's easier to swap a bunch of short messages than it is to interrupt each other's work at hand with a phone call. Furthermore, 99% of text messages are read while only 33% of voice-mail messages are heard; 95% of text messages are read within 3 minutes and, on average, responded to within 90 seconds.</p>

<p class="abs why-text" style="left:87px;top:2222px;width:421px">One of the many ways that Brackwell is bringing technology to its trade is through communication tools. A single point of contact gets you where you want to go. We distribute the text and email internally. Not only that, we share equal access to our communication points to hold each other accountable for their respective responsibilities. This flow of information is a more efficient, effective, and direct.</p>
<svg class="abs" style="left:770px;top:2222px" width="220" height="220" viewBox="0 0 220 220">
  <path d="M110 110V10A100 100 0 0 0 10 110Z" fill="var(--chart-green)"/>
  <path d="M110 110V10A100 100 0 0 1 210 110Z" fill="var(--blue-dark)"/>
  <path d="M110 110H210A100 100 0 0 1 110 210Z" fill="var(--chart-lime)"/>
  <path d="M110 110H10A100 100 0 0 0 110 210Z" fill="var(--blue-light)"/>
  <circle cx="110" cy="110" r="84" fill="#e4e4e4"/>
  <path d="M110 26V194M26 110H194" stroke="#fff" stroke-width="3"/>
  <circle cx="110" cy="110" r="16" fill="#fff" stroke="#ccc" stroke-width="2"/>
  <g font-family="Montserrat,sans-serif" fill="#555" text-anchor="middle">
    <text x="72" y="84" font-size="22">33%</text><text x="72" y="96" font-size="6">of adults</text>
    <text x="150" y="84" font-size="22">48%</text>
    <text x="72" y="150" font-size="22">78%</text><text x="72" y="162" font-size="6">of consumers</text>
    <text x="150" y="150" font-size="22">79%</text>
  </g>
</svg>
<div class="abs chart-label" style="left:615px;top:2168px;width:200px">33% of american adults prefertext to all other forms of communication (Lumen Survey)</div>
<div class="abs chart-label" style="left:970px;top:2168px;width:170px">Only 48% of businesses are equipped to handle messaging (Relay Labs)</div>
<div class="abs chart-label" style="left:615px;top:2334px;width:150px">78% of Consumers wish they could text business</div>
<div class="abs chart-label" style="left:1004px;top:2360px;width:150px">79%of bosses are supportive of texting for business purposes</div>

<div class="abs why-call">Call Us: <b>&#9742; 604-555-0182</b></div>
<div class="abs why-mail">hello@brackwellinteriors.com</div>
<a class="abs btn btn-outline" style="left:449px;top:2522px;width:144px">TRY IT NOW!</a>
<a class="abs btn btn-solid" style="left:605px;top:2522px;width:146px">CONTACT US</a>

<section>
  <h2 class="abs section-title testi-title">
    <svg class="title-bracket" viewBox="0 0 60 62"><path d="M40 2H14L2 14v46h36" fill="none" stroke="var(--orange)" stroke-width="3"/></svg>
    Happy <b>Customer</b></h2>
  <div class="abs quote-mark">&#8220;</div>
  <p class="abs testi-text">There are many variations of passages of Lorem Ipsum available, but the majority have suffered alteration in some form, by injected humour, or randomised words which don't look even slightly believable. If you are going to use a passage of Lorem Ipsum, you need to be sure there isn't anything embarrassing hidden in the ...</p>
  <div class="abs testi-name">STANDARD CHUNK</div>
  <div class="abs testi-dots"><span class="dot"></span><span class="dot on"></span><span class="dot"></span><span class="dot"></span></div>
</section>

<footer class="abs site-footer"></footer>
<div class="abs brand footer-brand"><span class="brand-mark"></span><span class="brand-name">BRACKWELL</span></div>
<div class="abs footer-head" style="left:87px;top:3340px">Contact Us</div>
<div class="abs footer-head" style="left:419px;top:3340px">Quick Links</div>
<div class="abs footer-head" style="left:593px;top:3340px">Send Us a Message</div>
<div class="abs footer-call">Call: 604-555-0182</div>
<div class="abs footer-small" style="left:87px;top:3430px">hello@brackwellinteriors.com</div>
<div class="abs footer-small" style="left:87px;top:3476px">4410 Harbour Line Rd<br>Eastfield, ML 30215</div>
<div class="abs social" style="left:87px;top:3532px"><span></span><span style="background:var(--orange)"></span><span></span></div>
<ul class="abs quick-links">
  <li>Home</li><li class="active">About Us</li><li>Services</li><li>Why Brackwell?</li><li>Projects</li><li>Contact Us</li>
</ul>
<div class="abs field" style="left:593px;top:3402px;width:163px">Name</div>
<div class="abs field" style="left:771px;top:3402px;width:164px">Phone</div>
<div class="abs field" style="left:950px;top:3402px;width:163px">Email</div>
<div class="abs field" style="left:593px;top:3447px;width:520px;height:104px">Message ..</div>
<svg class="abs send-btn" viewBox="0 0 28 28"><path d="M9 8l11 6-11 6 2-6z" fill="#fff"/></svg>
<div class="abs footer-bottom" style="left:87px">© 2019 <span style="color:var(--orange)">Brackwell</span>. All Rights Reserved</div>
<div class="abs footer-bottom" style="left:593px">Privacy Policy &nbsp;&nbsp;|&nbsp;&nbsp; Terms &amp; Conditions</div>
<svg class="abs" style="left:1104px;top:3634px" width="16" height="18" viewBox="0 0 16 18"><path d="M2 16 8 3l6 13M5 10h6" fill="none" stroke="var(--orange)" stroke-width="2"/></svg>

</body>
</html>
```